Website Design für Reinigungsunternehmen
Zielgruppe
Wir sind ein Reinigungsunternehmen, dass seit 2014 am Markt ist.
Was machen wir:
Das Angebot besteht darin, Räume nach dem IFSG (Infektionsschutzgesetz) und den Richtlinien des Werner Lasko Instituts mit ausgewählten Verfahren keimfrei zu bekommen.
Hygiene und prophylaktische Desinfektion sind für die Nutzung stark frequentierter Räume und Oberflächen gerade jetzt essentiell, denn die Ausbreitung von Viren und Bakterien kann auch durch präventive Maßnahmen eingedämmt werden.
Das Angebot ist, mit speziellen Reinigungsverfahren in Kombination mit Kaltverneblung ,die Räume fast vollständig von Keimen, Viren und Bakterien zu befreien.
So ist auch die Desinfektion von schwer zugänglichen Stellen und Gegenständen gewährleistet. Die eingesetzte Kaltnebeltechnologie wirkt in Verbindung mit Wasserstoffperoxid in verschiedenen Konzentrationen sowohl bakterizid, viruzid als auch fungizid. Wasserstoffperoxid wird rückstandsfrei abgebaut. Nach einer Einwirkzeit kann der behandelte, desinfizierte Raum sofort mechanisch gelüftet werden – ohne Material oder Umweltschäden zu riskieren.
Hier ein kurzes und erklärendes Video: https://klipvid.example/Qx7tmRwPaen
Aufgabenstellung
Die Website Soll maximal 3 Seiten haben.. Home (bzw. was wir machen..) Über uns (wer wir sind..) und Kontakt (-daten.
Ich möchte relativ kurz und knapp zum Thema kommen. Wenig Text, nur das wesentliche auf den Punkt gebracht - dafür ein ansprechendes professionelles Design. Bitte keine Bilder mit Gebäude, Reiniger etc. - dafür andere kreative Assoziationen einbringen.

```html
<!DOCTYPE html>
<html lang="de">
<head>
<meta charset="utf-8">
<title>Leistungen – Novar Group</title>
<link href="https://fonts.googleapis.com/css2?family=Montserrat:wght@400;500;600;700;800&display=swap" rel="stylesheet">
<style>
:root{
  --navy:#1f3160;
  --sky:#6aaad6;
  --white:#ffffff;
  --footer:#efefef;
  --field:#dedede;
  --ink:#1f3160;
}
*{margin:0;padding:0;box-sizing:border-box}
html,body{width:885px;height:1200px;overflow:hidden;background:var(--white)}
body{font-family:'Montserrat',sans-serif;color:var(--ink);position:relative}

/* nav */
.nav a{position:absolute;top:18px;height:22px;line-height:22px;font-size:9px;font-weight:600;color:var(--navy);text-decoration:none;letter-spacing:.2px}
.nav .home{left:338px}
.nav .active{left:397px;width:70px;text-align:center;border:1.2px solid var(--sky);border-radius:12px;color:var(--sky);font-weight:700}
.nav .kontakt{left:504px}

/* hero */
.splash{position:absolute;border-radius:50%}
.splash-left{left:-20px;top:95px;width:300px;height:110px;transform:rotate(-22deg);background:radial-gradient(ellipse at 60% 50%,#e9f3fa 0%,#b9d7ec 55%,rgba(255,255,255,0) 72%)}
.splash-right{left:600px;top:100px;width:310px;height:110px;transform:rotate(-20deg);background:radial-gradient(ellipse at 45% 50%,#e9f3fa 0%,#b9d7ec 55%,rgba(255,255,255,0) 72%)}
.hero-title{position:absolute;top:78px;left:0;width:885px;text-align:center;font-size:50px;font-weight:800;color:var(--navy);letter-spacing:-.5px}
.hero-sub{position:absolute;top:137px;left:0;width:885px;text-align:center;font-size:13px;line-height:12px;font-weight:700;color:var(--sky)}
.hero-kicker{position:absolute;top:197px;left:0;width:885px;text-align:center;font-size:8.5px;font-weight:700;color:var(--navy)}
.hero-text{position:absolute;top:222px;left:296px;width:293px;text-align:center;font-size:7.4px;line-height:8.9px;color:var(--navy)}

/* services band */
.band{position:absolute;left:0;top:299px;width:885px;height:763px;background:var(--navy)}
.card{position:absolute;left:173px;width:539px;height:170px;border-radius:24px;overflow:hidden;box-shadow:0 2px 3px rgba(0,0,0,.25)}
.card.blue{background:var(--sky);color:var(--white)}
.card.light{background:var(--white);color:var(--sky)}
.card .glow{position:absolute;left:345px;top:35px;width:200px;height:150px;border-radius:50%}
.card.blue .glow{background:radial-gradient(ellipse at center,rgba(255,255,255,.14) 0%,rgba(255,255,255,0) 70%)}
.card.light .glow{background:radial-gradient(ellipse at center,rgba(106,170,214,.12) 0%,rgba(106,170,214,0) 70%)}
.card .icon{position:absolute;left:19px;top:16px;width:31px;height:31px}
.card h2{position:absolute;left:59px;top:22px;font-size:12.8px;font-weight:700;white-space:nowrap}
.card .body{position:absolute;left:61px;top:61px;width:312px;font-size:6.6px;line-height:7.8px}
.card .body p+p{margin-top:8px}
.card ul{position:absolute;left:385px;top:60px;list-style:none;font-size:7px}
.card li{position:relative;padding-left:10px;height:11.2px;line-height:11.2px}
.card li::before{content:"";position:absolute;left:0;top:3.5px;width:4.5px;height:4.5px;border-radius:50%;background:currentColor}
.card .more{position:absolute;left:494px;top:138px;width:14px;height:10px}

/* call to action */
.cta-title{position:absolute;top:924px;left:0;width:885px;text-align:center;font-size:17.5px;line-height:17px;font-weight:700;color:var(--white)}
.cta-call{position:absolute;top:958px;left:0;width:885px;text-align:center;font-size:21px;font-weight:700;color:var(--sky)}
.phone-pill{position:absolute;left:372px;top:996px;width:155px;height:22px;border-radius:11px;background:var(--white)}
.phone-pill span{position:absolute;left:17px;top:0;line-height:22px;font-size:13px;font-weight:700;color:var(--navy)}
.phone-badge{position:absolute;left:357px;top:991px;width:30px;height:30px;border-radius:50%;background:var(--sky)}

/* footer */
.footer{position:absolute;left:0;top:1062px;width:885px;height:138px;background:var(--footer)}
.brand{position:absolute;left:173px;top:1081px;display:flex;align-items:center;gap:5px}
.brand i{display:block;width:14px;height:14px;border-radius:50%;background:var(--navy)}
.brand b{font-size:18px;font-weight:600;color:var(--navy);letter-spacing:-.3px}
.address{position:absolute;left:173px;top:1113px;font-size:7px;line-height:7.9px;color:var(--navy)}
.address strong{color:var(--sky);font-weight:700}
.f-head{position:absolute;top:1087px;font-size:6.6px;font-weight:700;color:var(--navy)}
.f-links{position:absolute;left:357px;top:1108px;font-size:7px;color:var(--navy);list-style:none}
.f-links li{height:15.8px}
.f-contact{position:absolute;left:449px;top:1108px;font-size:7px;color:var(--navy);list-style:none}
.f-contact li{height:15.8px;display:flex;align-items:flex-start;gap:4px}
.f-contact svg{width:9px;height:9px;flex:none}
.news-field{position:absolute;left:588px;top:1101px;width:124px;height:24px;border-radius:6px;background:var(--field)}
.news-field span{position:absolute;left:8px;top:0;line-height:24px;font-size:7px;font-style:italic;color:#a9a9a9}
.news-field svg{position:absolute;right:7px;top:8px;width:9px;height:7px}
.news-note{position:absolute;left:588px;top:1130px;width:125px;font-size:5.6px;line-height:6.3px;color:var(--navy)}
.rule{position:absolute;left:173px;top:1177px;width:539px;height:1px;background:#dcdcdc}
.rights{position:absolute;left:0;top:1186px;width:885px;text-align:center;font-size:5.6px;font-weight:500;color:var(--navy)}
.rights b{color:var(--sky);font-weight:700}
</style>
</head>
<body>

<nav class="nav">
  <a class="home" href="#">HOME</a>
  <a class="active" href="#">LEISTUNGEN</a>
  <a class="kontakt" href="#">KONTAKT</a>
</nav>

<div class="splash splash-left" role="img" aria-label="Wasserspritzer, frei gestellt, hellblau"></div>
<div class="splash splash-right" role="img" aria-label="Wasserspritzer mit Tropfen, frei gestellt, hellblau"></div>

<h1 class="hero-title">LEISTUNGEN</h1>
<p class="hero-sub">Flächen- und Raumdesinfektion<br>gem. IFSG § 17</p>
<p class="hero-kicker">NOVAR GROUP</p>
<p class="hero-text">Sed ut perspiciatis unde omnis iste natus error sit voluptatem accusantium doloremque laudantium, totam rem aperiam, eaque ipsa quae ab illo inventore veritatis et quasi architecto beatae vitae dicta sunt explicabo. Nemo enim ipsam voluptatem quia voluptas sit aspernatur aut odit aut fugit, sed quia consequuntur magni dolores eos qui ratione voluptatem sequi nesciunt.</p>

<section class="band"></section>

<article class="card blue" style="top:332px">
  <div class="glow" role="img" aria-label="Dezentes Wasser-Kreislauf-Motiv im Hintergrund"></div>
  <svg class="icon" viewBox="0 0 31 31" fill="none" stroke="#ffffff" stroke-width="1.8">
    <path d="M5 20 A12 12 0 0 1 24 6"/><path d="M26 11 A12 12 0 0 1 8 26"/>
    <path d="M21 3 L25 6 L21 9" stroke-width="1.5"/><path d="M11 23 L7 26 L11 29" stroke-width="1.5"/>
    <path d="M15.5 9 C13 13 11 15 11 18 a4.5 4.5 0 0 0 9 0 C20 15 18 13 15.5 9 Z" fill="#ffffff" stroke="none"/>
  </svg>
  <h2>Flächen- und Raumdesinfektion gem. IFSG § 17</h2>
  <div class="body">
    <p>Sed ut perspiciatis unde omnis iste natus error sit voluptatem accusantium doloremque laudantium, totam rem aperiam, eaque ipsa quae ab illo inventore veritatis et quasi architecto beatae vitae dicta sunt explicabo. Nemo enim ipsam voluptatem quia voluptas sit aspernatur aut odit aut fugit, sed quia consequuntur magni dolores eos qui ratione voluptatem sequi nesciunt.</p>
    <p>Neque porro quisquam est, qui dolorem ipsum quia dolor sit amet, consectetur, adipisci velit, sed quia non numquam eius modi tempora incidunt ut labore et dolore magnam aliquam quaerat voluptatem. Ut enim ad minima veniam.</p>
  </div>
  <ul><li>Sed ut perspiciatis</li><li>Voluptatem accusantium</li><li>Neque</li><li>Nemo enim ipsam</li><li>consectetur, adipisci velit</li></ul>
  <svg class="more" viewBox="0 0 14 10" fill="#ffffff"><path d="M5 0 L0 5 L5 10 L5 6.5 L14 6.5 L14 3.5 L5 3.5 Z"/></svg>
</article>

<article class="card light" style="top:527px">
  <div class="glow" role="img" aria-label="Dezentes Wasser-Kreislauf-Motiv im Hintergrund"></div>
  <svg class="icon" viewBox="0 0 31 31" fill="none" stroke="#6aaad6" stroke-width="1.8">
    <path d="M5 20 A12 12 0 0 1 24 6"/><path d="M26 11 A12 12 0 0 1 8 26"/>
    <path d="M21 3 L25 6 L21 9" stroke-width="1.5"/><path d="M11 23 L7 26 L11 29" stroke-width="1.5"/>
    <path d="M15.5 9 C13 13 11 15 11 18 a4.5 4.5 0 0 0 9 0 C20 15 18 13 15.5 9 Z" fill="#6aaad6" stroke="none"/>
  </svg>
  <h2>RKI gelistete und geprüfte Verfahren</h2>
  <div class="body">
    <p>Sed ut perspiciatis unde omnis iste natus error sit voluptatem accusantium doloremque laudantium, totam rem aperiam, eaque ipsa quae ab illo inventore veritatis et quasi architecto beatae vitae dicta sunt explicabo. Nemo enim ipsam voluptatem quia voluptas sit aspernatur aut odit aut fugit, sed quia consequuntur magni dolores eos qui ratione voluptatem sequi nesciunt.</p>
    <p>Neque porro quisquam est, qui dolorem ipsum quia dolor sit amet, consectetur, adipisci velit, sed quia non numquam eius modi tempora incidunt ut labore et dolore magnam aliquam quaerat voluptatem. Ut enim ad minima veniam.</p>
  </div>
  <ul><li>Sed ut perspiciatis</li><li>Voluptatem accusantium</li><li>Neque</li><li>Nemo enim ipsam</li><li>consectetur, adipisci velit</li></ul>
  <svg class="more" viewBox="0 0 14 10" fill="#6aaad6"><path d="M5 0 L0 5 L5 10 L5 6.5 L14 6.5 L14 3.5 L5 3.5 Z"/></svg>
</article>

<article class="card blue" style="top:722px">
  <div class="glow" role="img" aria-label="Dezentes Wasser-Kreislauf-Motiv im Hintergrund"></div>
  <svg class="icon" viewBox="0 0 31 31" fill="none" stroke="#ffffff" stroke-width="1.8">
    <path d="M5 20 A12 12 0 0 1 24 6"/><path d="M26 11 A12 12 0 0 1 8 26"/>
    <path d="M21 3 L25 6 L21 9" stroke-width="1.5"/><path d="M11 23 L7 26 L11 29" stroke-width="1.5"/>
    <path d="M15.5 9 C13 13 11 15 11 18 a4.5 4.5 0 0 0 9 0 C20 15 18 13 15.5 9 Z" fill="#ffffff" stroke="none"/>
  </svg>
  <h2>Staatlich geprüfte Desinfektoren</h2>
  <div class="body">
    <p>Sed ut perspiciatis unde omnis iste natus error sit voluptatem accusantium doloremque laudantium, totam rem aperiam, eaque ipsa quae ab illo inventore veritatis et quasi architecto beatae vitae dicta sunt explicabo. Nemo enim ipsam voluptatem quia voluptas sit aspernatur aut odit aut fugit, sed quia consequuntur magni dolores eos qui ratione voluptatem sequi nesciunt.</p>
    <p>Neque porro quisquam est, qui dolorem ipsum quia dolor sit amet, consectetur, adipisci velit, sed quia non numquam eius modi tempora incidunt ut labore et dolore magnam aliquam quaerat voluptatem. Ut enim ad minima veniam.</p>
  </div>
  <ul><li>Sed ut perspiciatis</li><li>Voluptatem accusantium</li><li>Neque</li><li>Nemo enim ipsam</li><li>consectetur, adipisci velit</li></ul>
  <svg class="more" viewBox="0 0 14 10" fill="#ffffff"><path d="M5 0 L0 5 L5 10 L5 6.5 L14 6.5 L14 3.5 L5 3.5 Z"/></svg>
</article>

<p class="cta-title">Vereinbaren Sie heute<br>noch einen Termin</p>
<p class="cta-call">Rufen Sie uns an</p>
<div class="phone-pill"><span>0991 / 555 210 40</span></div>
<div class="phone-badge">
  <svg viewBox="0 0 30 30" width="30" height="30"><path d="M10 8 l3 -1 l2.5 5 l-2 1.5 c1 2.5 3 4.5 5.5 5.5 l1.5 -2 l5 2.5 l-1 3 c-8 1 -15 -6 -14.5 -14.5 Z" fill="#ffffff"/></svg>
</div>

<footer class="footer"></footer>
<div class="brand"><i></i><b>novar</b></div>
<p class="address"><strong>NOVAR GROUP</strong><br>Gebäudereinigung &amp; Hygienekonzepte<br>Lindenweg 14<br>93999 Musterbach</p>

<p class="f-head" style="left:357px">QUICK LINKS</p>
<ul class="f-links"><li>HOME</li><li>LEISTUNGEN</li><li>KONTAKT</li></ul>

<p class="f-head" style="left:449px">KONTAKT UNS</p>
<ul class="f-contact">
  <li><svg viewBox="0 0 10 10"><path d="M2 1 l2 -0.5 l1.2 2.5 l-1 0.8 c0.5 1.2 1.5 2.2 2.7 2.7 l0.8 -1 l2.5 1.2 l-0.5 2 c-4 0.5 -8 -3.5 -7.7 -7.7 Z" fill="#6aaad6"/></svg>0991 / 555 210 40</li>
  <li><svg viewBox="0 0 10 10"><rect x="3" y="0.5" width="4" height="3" fill="#6aaad6"/><rect x="1" y="4" width="8" height="5" rx="1" fill="#6aaad6"/></svg>0991 / 555 210 49</li>
  <li><svg viewBox="0 0 10 10"><rect x="0.5" y="2" width="9" height="6.5" fill="#6aaad6"/><path d="M0.5 2 L5 5.5 L9.5 2" stroke="#ffffff" stroke-width=".8" fill="none"/></svg>info@novar-hygiene.example</li>
</ul>

<p class="f-head" style="left:588px">NEWSLETTER</p>
<div class="news-field"><span>Email address</span>
  <svg viewBox="0 0 9 7"><rect width="9" height="7" fill="#6aaad6"/><path d="M0 0 L4.5 3.5 L9 0" stroke="#ffffff" stroke-width=".8" fill="none"/></svg>
</div>
<p class="news-note">Lorem ipsum dolor sit amet, consectetur adipiscing elit</p>

<div class="rule"></div>
<p class="rights">ALL RIGHTS RESERVED BY <b>9FENNEL</b></p>

</body>
</html>
```